Expanding Agricultural services business needs a brochure in booklet style design

I currently have a small ag services business. We have been in business for 20 years. We now offer soil sampling and soil testing. we are expanding to offer new services which are corvalta seed sales and seed treatment. we want to get the word out about our expansion.....what we are offering......give brief detail about each service .......and let customers know that we are offering a "bundle" package to increase their productivity with a customer bonus reward program to earn free Farm Drainage Tiling.
Updates

Hello All,

Somehow my uploads of pictures and text did not end up on my project.  I have added back my pictures and in a couple hours will have text added.  Thank you for your patience!

Dolores

Would like this brochure in booklet style.....but if you think it would be better in another style....im open to about anything!

Thanks in advance

Hello again folks!

I have added my text.....and pix......sorry for the inconvenience

                                       

As it turns out......it seems 4 pages is not enought to get all my information out.  I believe I would like to stress the FENWRIGHT AG SERVICES EXPANSION 2013 .   We have offered soil testing services for 20 years and are expanding to offer Corvalta Seed  Sales and a new seed treatment facility.  We are putting together a Productivity Bundle......for increased yields, plus the opportunity to earn Drainage Tiling credits towards FREE Drainage Tiling.

It does not matter to me how many pages this ends up being.....I just need to get all my information in this booklet.

Thanks sooooo much

 

I must be able to edit my brochure after download.  It will need to be in an editable format.

Thanks

Target Market(s)

farmers

Industry/Entity Type

Business

Requirements
Must have
• I must be able to edit the brochure myself after download. So it will need to be in an editable format.
Nice to have
• farm related items...tractor...crops.....etc.

```html
<!DOCTYPE html>
<html lang="en">
<head>
<meta charset="utf-8">
<title>Fenwright Ag Services – Expansion 2013 Folder</title>
<link rel="stylesheet" href="https://fonts.googleapis.com/css2?family=Montserrat:wght@700;800&family=Didact+Gothic&display=swap">
<style>
  :root {
    --backdrop: #e8e5e0;
    --paper: #ffffff;
    --brand-red: #c8202a;
    --ink: #1d1d1d;
    --ink-soft: #444444;
    --sky: #a9cdea;
    --wheat: #e9b64a;
    --field-green: #3f8a2c;
    --soil: #3a2a1c;
    --ring-yellow: #f3d21c;
    --rule: #e3e3e3;
  }
  * { box-sizing: border-box; margin: 0; padding: 0; }
  html, body {
    width: 1200px; height: 955px; overflow: hidden;
    background: var(--backdrop);
  }
  .folder {
    position: absolute; left: 60px; top: 42px;
    width: 1080px; height: 870px;
    display: flex;
    box-shadow: 0 6px 24px rgba(0,0,0,.18);
  }
  .panel {
    position: relative; width: 540px; height: 870px;
    background: var(--paper); overflow: hidden;
  }
  .panel--left { border-right: 1px solid #d8d8d8; }
  .photo { position: absolute; left: 0; top: 0; width: 540px; height: 460px; }
  .photo--wheat {
    background: linear-gradient(180deg, var(--sky) 0%, #d9e6ee 28%, #f1d68a 48%, var(--wheat) 72%, #c9902c 100%);
  }
  .photo--field {
    background: linear-gradient(180deg, #cfe2f3 0%, #e6eef3 16%, #6aa84a 24%, var(--field-green) 55%, #2f5f22 80%, var(--soil) 100%);
  }
  .pocket { position: absolute; left: 0; top: 0; width: 540px; height: 870px; }

  .brand {
    position: absolute; left: 0; width: 540px; text-align: center;
    font-family: "Montserrat", sans-serif; font-weight: 800;
    color: var(--ink); line-height: 1.05; letter-spacing: .5px;
  }
  .brand__name { display: block; }
  .panel--left .brand { top: 500px; font-size: 24px; }
  .panel--right .brand { top: 470px; font-size: 32px; }

  .expansion-tag {
    position: absolute; left: 0; width: 540px; top: 462px; text-align: center;
    font-family: "Montserrat", sans-serif; font-weight: 700; font-size: 14px;
    letter-spacing: 3px; color: var(--brand-red);
  }
  .contact-box {
    position: absolute; left: 148px; top: 568px; width: 262px; height: 92px;
    background: var(--brand-red); color: #fff;
    font-family: "Didact Gothic", sans-serif; font-size: 13px;
    padding: 12px 18px; line-height: 1.6;
  }
  .contact-box .tel { font-family: "Montserrat", sans-serif; font-weight: 700; font-size: 16px; }
  .web {
    position: absolute; left: 0; width: 540px; top: 672px; text-align: center;
    font-family: "Didact Gothic", sans-serif; font-size: 14px; letter-spacing: .5px; color: var(--ink);
  }
  .web strong { color: var(--brand-red); font-family: "Montserrat", sans-serif; font-weight: 700; }

  .services {
    position: absolute; left: 30px; top: 712px; width: 480px;
    display: grid; grid-template-columns: 1fr 1fr; gap: 8px 16px;
    list-style: none; border-top: 1px solid var(--rule); padding-top: 10px;
  }
  .service__title {
    display: block; font-family: "Montserrat", sans-serif; font-weight: 700;
    font-size: 11.5px; color: var(--brand-red); letter-spacing: .3px;
  }
  .service__detail {
    display: block; font-family: "Didact Gothic", sans-serif;
    font-size: 11px; line-height: 1.35; color: var(--ink-soft);
  }

  .headline {
    position: absolute; left: 0; width: 540px; top: 580px; text-align: center;
    font-family: "Montserrat", sans-serif; font-weight: 700; font-size: 27px;
    color: var(--brand-red); line-height: 1.25; letter-spacing: .3px;
  }
  .rep {
    position: absolute; left: 0; width: 540px; top: 680px; text-align: center;
    font-family: "Didact Gothic", sans-serif; font-size: 20px; color: var(--ink);
  }
  .rep .phone { font-family: "Montserrat", sans-serif; font-weight: 700; font-size: 28px; margin-left: 6px; }
  .web-bar {
    position: absolute; left: 40px; top: 740px; width: 460px; height: 42px;
    background: var(--brand-red); color: #fff; text-align: center;
    font-family: "Didact Gothic", sans-serif; font-size: 14px; letter-spacing: 2px; line-height: 42px;
  }
  .bundle-note {
    position: absolute; left: 40px; top: 798px; width: 460px; text-align: center;
    font-family: "Didact Gothic", sans-serif; font-size: 13px; line-height: 1.45; color: var(--ink);
  }
  .bundle-note strong { font-family: "Montserrat", sans-serif; font-weight: 700; color: var(--brand-red); }
</style>
</head>
<body>
  <main class="folder">
    <section class="panel panel--left">
      <div class="photo photo--wheat" role="img" aria-label="Close-up photo of golden wheat ears against a blue sky"></div>
      <svg class="pocket" viewBox="0 0 540 870" aria-hidden="true">
        <polygon points="0,390 540,440 540,870 0,870" fill="var(--paper)"/>
        <polyline points="4,870 4,392 540,441" fill="none" stroke="var(--brand-red)" stroke-width="9"/>
      </svg>
      <p class="expansion-tag">EXPANSION 2013</p>
      <div class="brand">
        <span class="brand__name">FENWRIGHT</span>
        <span class="brand__name">AG SERVICES</span>
      </div>
      <div class="contact-box">
        <div>RR2 Box 41 Millbrook, IL 62519</div>
        <div>E : fenwrighttesting@fieldmail.com</div>
        <div>Tel: <span class="tel">217-555-0172</span></div>
      </div>
      <p class="web">www.<strong>fenwrightagservice</strong>.com</p>
      <ul class="services">
        <li class="service">
          <span class="service__title">SOIL SAMPLING &amp; TESTING</span>
          <span class="service__detail">20 years of trusted field sampling and lab-backed soil analysis.</span>
        </li>
        <li class="service">
          <span class="service__title">CORVALTA SEED SALES</span>
          <span class="service__detail">Proven seed genetics matched to your soil test results.</span>
        </li>
        <li class="service">
          <span class="service__title">SEED TREATMENT</span>
          <span class="service__detail">Our new treatment facility protects seed from planting onward.</span>
        </li>
        <li class="service">
          <span class="service__title">PRODUCTIVITY BUNDLE</span>
          <span class="service__detail">Testing, seed and treatment together for increased yields.</span>
        </li>
      </ul>
    </section>

    <section class="panel panel--right">
      <div class="photo photo--field" role="img" aria-label="Photo of long green crop rows stretching across a tilled field"></div>
      <svg class="pocket" viewBox="0 0 540 870">
        <circle cx="372" cy="160" r="104" fill="var(--soil)" stroke="var(--ring-yellow)" stroke-width="7" role="img" aria-label="Inset photo of cupped hands holding soil with a young seedling"/>
        <polygon points="0,445 540,395 540,870 0,870" fill="var(--paper)" aria-hidden="true"/>
        <polyline points="0,446 536,396 536,870" fill="none" stroke="var(--brand-red)" stroke-width="9" aria-hidden="true"/>
      </svg>
      <div class="brand">
        <span class="brand__name">FENWRIGHT</span>
        <span class="brand__name">AG SERVICES</span>
      </div>
      <h1 class="headline">CROP HEALTH CONCENTRATION<br>CROP YIELD DOMINATION!</h1>
      <p class="rep">Dolores Hartwell -<span class="phone">217-555-0148</span></p>
      <div class="web-bar">www.fenwrightagservice.com</div>
      <p class="bundle-note"><strong>Bonus Rewards:</strong> every Productivity Bundle earns credits<br>toward <strong>FREE Farm Drainage Tiling</strong>.</p>
    </section>
  </main>
</body>
</html>
```